CoinLantern one-page corporate website

Our company, CoinLantern is a cryptocurrency Initial Coin Offering ("ICO" marketing and promotion agency, which requires a professional company landing page design whereby prospective clients can learn;
-who we are
-what we do
-what our people are saying about us
-core team members
-subscribe to our mailing list
-how to get in touch (basic contact form)

We are looking for something unique and attractive -- not a standard Vanto template that we could put together ourselves. Plain stock images should not be used. Unique visualizations of the service offerings and creative presentation are key. We are a cutting edge marketing agency and as such, we need to look the part.

Relevant documentation about the business and branding assets have been attached to guide the designer. Certain information will be included by the company at a later date such as team member descriptions. As such, lorem ipsum may be included wherever necessary to help visualize the textual areas.

****Please ensure that you actually utilize the photos and graphics provided so that we can have a good picture of what it would actually look like with our branding.

The site must be responsive HTML CSS Design.

Sites style themes we like for inspiration and specific sections we like ****Very important***:
https://fundrivermesh.com/offers - we like that the token & company logo is used in unique visualizations that connects various ideas together. We imagine unique visuals such as these with our Icon (see attached) serving as a token. We also like the unique and attractive visual theme of the webpage itself.

https://pavoniaholdings.com/ - we like the layout of this website, specifically how the service offerings are displayed in a circular visual graphic with the Pavonia logo in the middle. We imagine a similar type of graphic designed with CoinLantern in the middle.

https://quorvanet.org/ - we like how the logo is central to the theme in this site when you first enter and how it fades + shrinks into the distance as you scroll down.

Target Market(s)

cryptocurrency entrepreneurs and ICOs

Industry/Entity Type

It Company

Coding

Coded - Design and coding required

Number of Pages Required

1 page

Font styles to use
Sans Serif

Colors

Designer to choose colors to be used in the design.

Requirements
Must have
• The site must be responsive HTML CSS Design.
• The page must be modern and visually attractive. Elements must not be static and should have a fluid motion / visual change as the user scrolls through the page.
Should not have
• The project should not use any old stock images or elements which are dull and over-used, but rather images or elements should be unique and well thought out.

```html
<!DOCTYPE html>
<html lang="en">
<head>
<meta charset="utf-8">
<title>CoinLantern — ICO Marketing Agency</title>
<link href="https://fonts.googleapis.com/css2?family=Michroma&family=Roboto:wght@400;500;700&family=Roboto+Condensed:wght@400;700&display=swap" rel="stylesheet">
<style>
:root{
  --navy:#1c3d6b;
  --navy-dark:#14325a;
  --ink:#1b2a3d;
  --sky:#1aa3e6;
  --sky-dark:#1386c8;
  --blue-deep:#1b4a8a;
  --grey-bg:#efeff0;
  --text:#555b63;
  --footer:#232323;
  --footer-field:#4a4a4a;
  --white:#ffffff;
}
*{margin:0;padding:0;box-sizing:border-box}
html,body{width:1200px;height:3321px;overflow:hidden}
body{position:relative;font-family:"Roboto",Arial,sans-serif;color:var(--text);background:var(--white)}
.abs{position:absolute}

/* top strip */
.top-strip{left:0;top:0;width:1200px;height:31px;background:var(--white)}
.top-strip .social-dot{position:absolute;top:9px;width:12px;height:12px;border-radius:50%;background:var(--navy)}

/* nav */
.nav{left:0;top:31px;width:1200px;height:64px;background:linear-gradient(90deg,var(--navy-dark),var(--navy) 60%,#1f4677)}
.brand{position:absolute;left:160px;top:8px;display:flex;align-items:center;gap:10px}
.brand-mark{width:48px;height:48px;border-radius:50%;border:3px solid var(--white)}
.brand-name{font-family:"Michroma",sans-serif;font-size:22px;color:var(--white)}
.nav-links{position:absolute;left:595px;top:0;height:64px;display:flex}
.nav-links a{display:block;height:64px;line-height:64px;padding:0 14px;color:var(--white);font-family:"Roboto Condensed",sans-serif;font-size:12.5px;text-decoration:none;text-transform:uppercase;margin-right:14px}
.nav-links a.active{background:var(--sky)}

/* hero */
.hero{left:0;top:95px;width:1200px;height:476px;background:
  radial-gradient(ellipse 700px 140px at 30% 62%,rgba(200,214,230,.45),transparent 70%),
  radial-gradient(ellipse 600px 120px at 80% 40%,rgba(210,222,236,.5),transparent 70%),
  linear-gradient(180deg,#fdfdfe,#f2f5f9 60%,#fbfcfd)}
.hero-title{left:0;width:1200px;top:84px;text-align:center;font-family:"Michroma",sans-serif;font-size:24px;font-weight:400;color:var(--navy)}
.hero-sub{left:0;width:1200px;top:126px;text-align:center;font-family:"Roboto Condensed",sans-serif;font-size:22px;color:var(--navy)}
.hero-signup{left:0;width:1200px;top:208px;text-align:center;font-family:"Michroma",sans-serif;font-size:19px;font-weight:400;color:var(--ink)}
.signup-field{left:387px;top:264px;width:310px;height:40px;background:var(--white);border:1px solid #e2e6ea;font-size:12px;color:#9aa2ab;padding:12px 14px}
.signup-btn{left:697px;top:264px;width:127px;height:40px;background:var(--sky);color:var(--white);font-family:"Roboto Condensed",sans-serif;font-weight:700;font-size:13px;text-align:center;line-height:40px;clip-path:polygon(0 0,100% 0,94% 100%,0 100%)}
.scroll-cue{left:574px;top:377px}

/* how it works */
.how{left:0;top:571px;width:1200px;height:452px;background:radial-gradient(circle at 600px 230px,#ffffff 0,#f4f4f5 200px,var(--grey-bg) 420px)}
.section-title{position:absolute;left:0;width:1200px;text-align:center;font-family:"Michroma",sans-serif;font-size:17px;font-weight:400;color:#111}
.rule{position:absolute;left:583px;width:34px;height:2px;background:var(--sky)}
.how-copy{left:190px;width:820px;font-size:11px;line-height:19px;text-align:center;color:#444}
.step{position:absolute;top:264px;display:flex;align-items:center;gap:7px;white-space:nowrap;font-family:"Michroma",sans-serif;font-size:9px;color:var(--navy)}
.step-num{flex:none;width:28px;height:28px;border:2px solid var(--navy);border-radius:50%;text-align:center;line-height:24px;font-family:"Roboto",sans-serif;font-size:14px}
.learn-btn{left:536px;top:339px;width:126px;height:40px;background:var(--sky);color:var(--white);font-family:"Roboto Condensed",sans-serif;font-weight:700;font-size:13px;text-align:center;line-height:40px;clip-path:polygon(6% 0,100% 0,94% 100%,0 100%)}

/* what we do */
.services{left:0;top:1023px;width:1200px;height:598px;background:linear-gradient(110deg,var(--blue-deep) 0%,#1b67ad 45%,#1799dc 100%)}
.services .rule{background:var(--white)}
.svc{position:absolute;display:flex;align-items:center;gap:9px;white-space:nowrap;font-family:"Michroma",sans-serif;font-size:11px;line-height:14px;color:var(--white);text-transform:uppercase}
.svc.left{justify-content:flex-end;text-align:right}
.svc.right{text-align:left}
.svc-num{flex:none;width:34px;height:34px;border:2px solid var(--white);border-radius:50%;text-align:center;line-height:30px;font-family:"Roboto",sans-serif;font-size:15px}
.hub-name{left:0;width:1200px;top:340px;text-align:center;font-family:"Michroma",sans-serif;font-size:26px;color:var(--white)}

/* team */
.team{left:0;top:1621px;width:1200px;height:617px;background:radial-gradient(ellipse at 50% 55%,#fafafa 0,#ececec 70%)}
.member-photo{position:absolute;background:var(--white);padding:5px;box-shadow:0 2px 6px rgba(0,0,0,.2)}
.member-photo .fill{width:100%;height:100%}
.member-photo::before,.member-photo::after{content:"";position:absolute;left:-6px;right:-6px;height:4px;background:#2b2b2b}
.member-photo::before{top:-8px}
.member-photo::after{bottom:-8px}
.member{position:absolute;width:240px}
.member h3{font-family:"Michroma",sans-serif;font-size:11px;font-weight:400;color:#222;margin-bottom:14px}
.member p{font-size:11px;line-height:18px;color:#555;margin-bottom:12px}
.member a{font-size:11px;color:var(--sky);text-decoration:none}

/* video */
.video{left:0;top:2238px;width:1200px;height:366px;background:linear-gradient(100deg,#173e6f 0%,#1f5e9f 45%,#2a78bd 75%,#3b8ccc 100%)}
.play{left:566px;top:152px}

/* testimonials */
.testimonials{left:0;top:2604px;width:1200px;height:354px;background:linear-gradient(180deg,#ffffff,#f5f7fa 50%,#ffffff)}
.quote-mark{left:0;width:1200px;top:118px;text-align:center;font-family:Georgia,serif;font-size:54px;line-height:40px;color:#d4d8dd}
.quote-text{left:270px;width:660px;top:163px;text-align:center;font-size:11px;line-height:20px;color:#444}
.quote-by{left:0;width:1200px;top:216px;text-align:center;font-size:12px;color:#333}
.pager{position:absolute;top:274px;width:32px;height:32px;border:1px solid #c9ced4;border-radius:50%}

/* footer */
.footer{left:0;top:2958px;width:1200px;height:363px;background:var(--footer)}
.foot-h{position:absolute;font-family:"Roboto Condensed",sans-serif;font-size:13.5px;color:var(--white);text-transform:uppercase}
.foot-line{position:absolute;height:3px;background:linear-gradient(90deg,#5e7388,#2d5b86)}
.field{position:absolute;background:var(--footer-field);color:#ddd;font-size:12px;padding:12px 14px}
.submit{left:160px;top:232px;width:128px;height:38px;background:var(--sky);color:var(--white);font-family:"Roboto Condensed",sans-serif;font-weight:700;font-size:13px;text-align:center;line-height:38px;clip-path:polygon(0 0,100% 0,92% 100%,0 100%)}
.quick-links{left:618px;top:64px;list-style:none}
.quick-links li{font-size:11.5px;line-height:19.5px;color:#cfd3d7}
.quick-links li::before{content:"›";color:var(--sky);margin-right:8px}
.social-box{position:absolute;top:164px;width:37px;height:37px}
.copyright{left:160px;top:337px;font-size:11px;color:#aaa}
.copyright b{color:var(--sky);font-weight:400}
.legal{right:160px;top:337px;font-size:11px;color:#ccc}
</style>
</head>
<body>

<header class="abs top-strip">
  <span class="social-dot" style="left:160px" aria-label="Social profile"></span>
  <span class="social-dot" style="left:182px" aria-label="Social profile"></span>
  <span class="social-dot" style="left:204px" aria-label="Social profile"></span>
  <span class="social-dot" style="left:226px" aria-label="Social profile"></span>
</header>

<nav class="abs nav">
  <div class="brand"><span class="brand-mark"></span><span class="brand-name">CoinLantern</span></div>
  <div class="nav-links">
    <a class="active" href="#">Home</a>
    <a href="#">Who We Are</a>
    <a href="#">What We Do</a>
    <a href="#">Testimonial</a>
    <a href="#">Contact</a>
  </div>
</nav>

<section class="abs hero">
  <h1 class="abs hero-title">CoinLantern</h1>
  <p class="abs hero-sub">Our Tight-Knit Group Of Experts Becomes A Part Of Your Team</p>
  <h2 class="abs hero-signup">SIGN UP FOR ICO NEWS &amp; ALERTS</h2>
  <div class="abs signup-field">email address</div>
  <div class="abs signup-btn">SIGN UP</div>
  <svg class="abs scroll-cue" width="52" height="52" viewBox="0 0 52 52">
    <circle cx="26" cy="26" r="24" fill="none" stroke="#3a5a80" stroke-width="2"/>
    <path d="M17 22l9 9 9-9" fill="none" stroke="#3a5a80" stroke-width="2.4"/>
  </svg>
</section>

<section class="abs how">
  <h2 class="section-title" style="top:86px">HOW DOES IT WORK</h2>
  <div class="rule" style="top:118px"></div>
  <p class="abs how-copy" style="top:141px">Our tight-knit group of experts becomes a part of your team for the crucial period leading up to and during your ICO. We take the time to thoroughly understand your project and the people behind it. By drawing on our deep expertise in the space and network of valuable connections,</p>
  <p class="abs how-copy" style="top:199px">we work closely with you to develop and implement the steps involved in executing a successful ICO. Best practices, market conditions, and investor psychology are constantly changing. We stay laser-focused on the ICO segment of the cryptocurrency landscape to stay up to date.</p>
  <div class="step" style="left:172px"><span class="step-num">1</span>SUBMIT APPLICATION</div>
  <div class="step" style="left:388px"><span class="step-num">2</span>CONFERENCE CALL WITH EXPERT</div>
  <div class="step" style="left:671px"><span class="step-num">3</span>SIGN AGREEMENT</div>
  <div class="step" style="left:852px"><span class="step-num">4</span>LET THE MAGIC BEGIN</div>
  <div class="abs learn-btn">LEARN MORE</div>
</section>

<section class="abs services">
  <h2 class="section-title" style="top:66px;color:var(--white)">WHAT WE DO</h2>
  <div class="rule" style="top:98px"></div>
  <svg class="abs" style="left:400px;top:136px" width="400" height="400" viewBox="0 0 400 400">
    <path d="M200 24 A176 176 0 0 1 360 296" fill="none" stroke="#fff" stroke-width="9" stroke-linecap="round"/>
    <path d="M360 296 A176 176 0 0 1 60 310" fill="none" stroke="#fff" stroke-width="9" stroke-linecap="round"/>
    <path d="M40 150 A164 164 0 0 1 150 40" fill="none" stroke="#fff" stroke-width="9" stroke-linecap="round"/>
    <circle cx="200" cy="150" r="30" fill="none" stroke="#fff" stroke-width="3"/>
  </svg>
  <div class="abs hub-name">CoinLantern</div>

  <div class="svc left" style="top:142px;right:713px">Whitepaper Consultation<br>and Review<span class="svc-num">1</span></div>
  <div class="svc left" style="top:202px;right:764px">Raise Amount and Future<br>Token Price Strategy<span class="svc-num">2</span></div>
  <div class="svc left" style="top:266px;right:790px">Token Sale Strategy<span class="svc-num">3</span></div>
  <div class="svc left" style="top:332px;right:790px">KYC (Know Your<br>Customer) Strategies<span class="svc-num">4</span></div>
  <div class="svc left" style="top:399px;right:773px">Secure Token<br>Launch Website<span class="svc-num">5</span></div>
  <div class="svc left" style="top:465px;right:724px">News and Press Related<br>Strategies and Execution<span class="svc-num">6</span></div>

  <div class="svc right" style="top:142px;left:740px"><span class="svc-num">7</span>Whitepaper Consultation<br>and Review</div>
  <div class="svc right" style="top:202px;left:789px"><span class="svc-num">8</span>Raise Amount and Future<br>Token Price Strategy</div>
  <div class="svc right" style="top:266px;left:815px"><span class="svc-num">9</span>Token Sale Strategy</div>
  <div class="svc right" style="top:332px;left:818px"><span class="svc-num">10</span>KYC (Know Your<br>Customer) Strategies</div>
  <div class="svc right" style="top:399px;left:800px"><span class="svc-num">11</span>Secure Token<br>Launch Website</div>
  <div class="svc right" style="top:465px;left:754px"><span class="svc-num">12</span>News and Press Related<br>Strategies and Execution</div>
</section>

<section class="abs team">
  <h2 class="section-title" style="top:70px">CORE TEAM MEMBERS</h2>
  <div class="rule" style="top:102px"></div>

  <div class="member-photo" style="left:173px;top:150px;width:277px;height:104px;transform:rotate(-1.5deg)">
    <div class="fill" role="img" aria-label="Portrait of Dorian Vell at a conference" style="background:linear-gradient(90deg,#2a5fa6,#6f89a8 55%,#c9d2dc)"></div>
  </div>
  <div class="member" style="left:480px;top:152px">
    <h3>DORIAN VELL</h3>
    <p>Duis aute irure dolor in reprehenderit in voluptate velit esse cillum dolore eu fugiat nulla pariatur.</p>
    <p>Excepteur sint occaecat cupidatat non proident, sunt in culpa qui officia</p>
    <a href="#">Read More</a>
  </div>

  <div class="member-photo" style="left:753px;top:150px;width:277px;height:102px;transform:rotate(1.2deg)">
    <div class="fill" role="img" aria-label="Portrait of Elian Brooke by a lake" style="background:linear-gradient(180deg,#b9cde2,#7f98b0 55%,#4d5a66)"></div>
  </div>

  <div class="member" style="left:160px;top:356px">
    <h3>MARCUS TOLLE</h3>
    <p>Duis aute irure dolor in reprehenderit in voluptate velit esse cillum dolore eu fugiat nulla pariatur.</p>
    <p>Excepteur sint occaecat cupidatat non proident, sunt in culpa qui officia</p>
    <a href="#">Read More</a>
  </div>

  <div class="member-photo" style="left:458px;top:358px;width:279px;height:164px;transform:rotate(-.6deg)">
    <div class="fill" role="img" aria-label="Portrait of Marcus Tolle outdoors beside a car" style="background:linear-gradient(180deg,#9fb7c9,#7a8c7a 55%,#3a3a36)"></div>
  </div>

  <div class="member" style="left:782px;top:372px">
    <h3>ELIAN BROOKE</h3>
    <p>Duis aute irure dolor in reprehenderit in voluptate velit esse cillum dolore eu fugiat nulla pariatur.</p>
    <p>Excepteur sint occaecat cupidatat non proident, sunt in culpa qui officia</p>
    <a href="#">Read More</a>
  </div>
</section>

<section class="abs video" role="img" aria-label="Video still of a team member speaking in an office, tinted blue">
  <svg class="abs play" width="66" height="66" viewBox="0 0 66 66">
    <path d="M33 4 A29 29 0 1 1 10 50" fill="none" stroke="#fff" stroke-width="3"/>
    <path d="M33 62 A29 29 0 0 1 6 24" fill="none" stroke="#fff" stroke-width="3" opacity=".8"/>
    <path d="M27 21 L46 33 L27 45 Z" fill="#fff"/>
  </svg>
</section>

<section class="abs testimonials">
  <h2 class="section-title" style="top:70px">WHAT OUR PEOPLE ARE SAYING ABOUT US</h2>
  <div class="rule" style="top:103px"></div>
  <div class="abs quote-mark">“</div>
  <p class="abs quote-text">Lorem ipsum dolor sit amet, consectetur adipiscing elit, sed do eiusmod tempor incididunt ut labore et dolore magna aliqua. Ut enim ad minim veniam, quis nostrud exercitation ullamco laboris nisi ut aliquip ex ea commodo consequat.</p>
  <p class="abs quote-by">Aaron Pell - Friday 25/11</p>
  <svg class="pager" style="left:564px" viewBox="0 0 32 32"><path d="M18 11l-5 5 5 5" fill="none" stroke="#9aa2ab" stroke-width="1.6"/></svg>
  <svg class="pager" style="left:604px" viewBox="0 0 32 32"><path d="M14 11l5 5-5 5" fill="none" stroke="#9aa2ab" stroke-width="1.6"/></svg>
</section>

<footer class="abs footer">
  <h4 class="foot-h" style="left:160px;top:32px">Contact Us</h4>
  <div class="foot-line" style="left:160px;top:56px;width:238px"></div>
  <div class="field" style="left:160px;top:93px;width:190px;height:38px">Name</div>
  <div class="field" style="left:354px;top:93px;width:193px;height:38px">Email</div>
  <div class="field" style="left:160px;top:137px;width:387px;height:87px">Message</div>
  <div class="abs submit">SUBMIT</div>

  <h4 class="foot-h" style="left:618px;top:32px">Quick Links</h4>
  <ul class="abs quick-links">
    <li>Home</li><li>Who We Are</li><li>What We Do</li><li>Testimonial</li><li>Contact Us</li>
  </ul>

  <h4 class="foot-h" style="left:788px;top:32px">Newsletter Sign Up</h4>
  <div class="foot-line" style="left:788px;top:56px;width:250px"></div>
  <div class="field" style="left:788px;top:93px;width:250px;height:38px">email address</div>
  <svg class="abs" style="left:1010px;top:106px" width="18" height="12" viewBox="0 0 18 12"><rect x="1" y="1" width="16" height="10" fill="#e6e6e6"/><path d="M1 1l8 6 8-6" fill="none" stroke="#4a4a4a" stroke-width="1.3"/></svg>
  <span class="social-box" style="left:788px;background:#2f5597" aria-label="Social profile"></span>
  <span class="social-box" style="left:832px;background:#1aa3e6" aria-label="Social profile"></span>
  <span class="social-box" style="left:878px;background:#c8433a" aria-label="Social profile"></span>
  <span class="social-box" style="left:923px;background:#1f78b4" aria-label="Social profile"></span>

  <p class="abs copyright">Copyrights ©2017 <b>CoinLantern</b> Allrights are Reserved.</p>
  <p class="abs legal">Privacy Policy &nbsp;|&nbsp; Terms And Condition</p>
</footer>

</body>
</html>
```